Penselbo.com

I want to change my current web site penselbo.com to become a word press theme site instead. My audience is art people mainly in the age between 25 to 50.
I want to keep some of the feel of the web site but want it to be more fresh and I want the base colors to be more light.
I want it to have a gallery function which I can use for showing new and existing artwork.
There need to be possibilities to create categories that can be well promoted on the front page. I want the front page to consist of: description of the web site with both text and image, two category blocks on which I can promote featured material, one block with the gallery and below the latest posts.
Apart from this I want the theme to work as a traditional wordpress blog with comment functions etc.
Looking forward to see your magic =)
Target Market(s)
Art people in Sweden in the age between 25 to 50, equal amount of male and female, but I want the theme to be leaning toward the female side.
Requirements
Must have
- I need one front page (see above), one gallery page, one page with a text post, one listing page and one contact page.
Nice to have
- Please make some new suggestions for the logo, you can use the current one as a role but try to make it more new and fresh.

```html
<!DOCTYPE html>
<html lang="sv">
<head>
<meta charset="utf-8">
<title>Penselbo.com – Genuin Svensk Konst I Akvarell</title>
<link rel="stylesheet" href="https://fonts.googleapis.com/css2?family=Arimo:wght@400;700&family=Tinos:wght@400;700&display=swap">
<style>
  :root {
    --page-bg: #e9e2d6;
    --swirl: #d8cebd;
    --column-edge: #d2c7b5;
    --column-bg: #efe9de;
    --header-bg: #d9ccb7;
    --header-ink: #4a4034;
    --panel: #fbf9f4;
    --panel-border: #d6cebf;
    --ink: #2c2a26;
    --muted-ink: #4a4740;
    --title-grey: #5e6152;
    --title-olive: #6a5630;
    --link: #7a6530;
    --footer-bar: #f1ebda;
    --button-dark: #9c8c70;
    --button-light: #c8b89a;
  }
  * { box-sizing: border-box; margin: 0; padding: 0; }
  html, body { width: 1200px; height: 496px; overflow: hidden; }
  body {
    position: relative;
    background: var(--page-bg);
    font-family: "Arimo", Arial, sans-serif;
    color: var(--ink);
  }
  .swirl-decor { position: absolute; top: 0; height: 496px; }
  .swirl-decor.left { left: 0; width: 211px;
    background: radial-gradient(ellipse at 45% 35%, var(--swirl) 0%, transparent 65%); }
  .swirl-decor.right { right: 0; width: 211px;
    background: radial-gradient(ellipse at 50% 100%, var(--swirl) 0%, transparent 55%); }

  .site {
    position: absolute; left: 211px; top: 0; width: 778px; height: 496px;
    background: var(--column-bg);
    border-left: 11px solid var(--column-edge);
    border-right: 11px solid var(--column-edge);
  }
  .site-header {
    position: absolute; left: 0; top: 0; width: 756px; height: 84px;
    background: var(--header-bg);
  }
  .brand {
    position: absolute; left: 40px; top: 36px;
    display: flex; align-items: center; gap: 7px;
    font-family: "Tinos", serif; font-size: 14px; letter-spacing: 1px;
    text-transform: uppercase; color: var(--header-ink);
  }
  .brand-dot { width: 9px; height: 9px; border-radius: 50%; background: #a48f6a; }
  .tagline {
    position: absolute; left: 315px; top: 34px;
    font-family: "Tinos", serif; font-size: 16px; letter-spacing: 2.8px; color: var(--header-ink);
  }

  .main-nav {
    position: absolute; left: 7px; top: 87px; height: 22px;
    display: flex; align-items: center; font-size: 10px; color: #4a4238;
  }
  .main-nav a { color: inherit; text-decoration: none; }
  .main-nav .sep { color: #8a7e6a; }
  .main-nav a.current {
    width: 56px; height: 22px; line-height: 22px; text-align: center; border-radius: 2px;
    background: linear-gradient(var(--button-light), var(--button-dark));
    color: #fff; margin-right: 4px;
  }
  .main-nav .sep { margin: 0 19px 0 0; }
  .main-nav a:not(.current) { margin-right: 20px; }

  .panel {
    position: absolute; background: var(--panel);
    border: 1px solid var(--panel-border); border-radius: 5px;
    box-shadow: 0 1px 2px rgba(90,75,50,.25);
  }
  .widget { left: 12px; width: 202px; padding: 10px 12px; }
  .widget-title { font-size: 11px; font-weight: 700; display: flex; align-items: center; gap: 6px; }
  .gallery-grid { display: grid; grid-template-columns: 68px 68px; gap: 6px; margin-top: 24px; }
  .thumb { height: 46px; border: 1px solid #cfc8b8; }
  .thumb.t1 { background: linear-gradient(135deg, #4e6a48, #8b9c98); }
  .thumb.t2 { background: linear-gradient(135deg, #c2aed0, #d88aa0); }
  .thumb.t3 { background: linear-gradient(135deg, #f8e69a, #efc06a); }
  .thumb.t4 { background: linear-gradient(#6a6a88, #d09a5a 45%, #4a5a3a 60%); }
  .search-field { margin-top: 15px; width: 174px; height: 19px; border: 1px solid #9aa8b8; background: #fff; }
  .button {
    margin-top: 1px; width: 64px; height: 24px; border-radius: 3px; border: 0;
    background: linear-gradient(var(--button-light), var(--button-dark) 60%);
    color: #fff; font: 10px "Arimo", Arial, sans-serif;
  }
  .cat-list { list-style: none; margin-top: 20px; font-size: 10px; }
  .cat-list li { display: flex; align-items: center; gap: 6px; }
  .cat-list a { color: #7a786c; }

  .post { left: 231px; width: 517px; padding: 13px 13px; }
  .post-title { font-size: 19px; font-weight: 700; color: var(--title-grey); line-height: 24px; }
  .post-meta { font-size: 9px; margin-top: 6px; }
  .post-meta a, .post-footer a { color: var(--link); }
  .post-body { display: flex; gap: 10px; margin-top: 8px; font-size: 9.5px; line-height: 12.6px; color: var(--muted-ink); text-align: justify; }
  .post-body p { flex: 1; }
  .feature-image { flex: none; width: 224px; height: 173px; margin-top: 9px;
    background: radial-gradient(ellipse at 50% 60%, #dccca8, #b09670 80%); }
  .post-footer {
    margin-top: 11px; padding: 3px 3px; font-size: 9px;
    background: var(--footer-bar); border: 1px solid #ddd3b8;
  }

  .category-block { width: 254px; padding: 11px 12px; top: 410px; height: 110px; }
  .category-block.first { left: 231px; }
  .category-block.second { left: 494px; }
  .category-label { font-size: 8.5px; text-transform: uppercase; letter-spacing: 1px; color: var(--link); }
  .category-title { font-size: 16px; font-weight: 700; color: var(--title-olive); margin-top: 3px; }
  .category-body { display: flex; gap: 8px; margin-top: 6px; font-size: 9.5px; line-height: 12.6px; color: var(--muted-ink); }
  .category-image { flex: none; width: 90px; height: 50px; }
  .category-image.landscape { background: linear-gradient(#8c7c8a, #b89a92); }
  .category-image.exhibit { background: linear-gradient(#cfc2a8, #a89676); }
</style>
</head>
<body>
  <div class="swirl-decor left" role="img" aria-label="Dekorativt virvelmönster"></div>
  <div class="swirl-decor right" role="img" aria-label="Dekorativt virvelmönster"></div>

  <div class="site">
    <header class="site-header">
      <div class="brand"><span class="brand-dot"></span>Penselbo.com</div>
      <div class="tagline">Genuin Svensk Konst I Akvarell</div>
    </header>

    <nav class="main-nav">
      <a class="current" href="#">Home</a><span class="sep">|</span>
      <a href="#">About Us</a><span class="sep">|</span>
      <a href="#">Gallery</a><span class="sep">|</span>
      <a href="#">Directory</a><span class="sep">|</span>
      <a href="#">Contact Us</a>
    </nav>

    <aside>
      <section class="panel widget" style="top:123px;height:157px">
        <h3 class="widget-title"><svg width="9" height="13" viewBox="0 0 9 13"><path d="M1 1 L8 6.5 L1 12 Z" fill="none" stroke="#444" stroke-width="1.2"/></svg>Gallery</h3>
        <div class="gallery-grid">
          <div class="thumb t1" role="img" aria-label="Akvarell: träd vid vatten"></div>
          <div class="thumb t2" role="img" aria-label="Akvarell: hjärta"></div>
          <div class="thumb t3" role="img" aria-label="Akvarell: gula blommor"></div>
          <div class="thumb t4" role="img" aria-label="Akvarell: solnedgång över äng"></div>
        </div>
      </section>

      <section class="panel widget" style="top:294px;height:93px">
        <h3 class="widget-title"><svg width="9" height="13" viewBox="0 0 9 13"><path d="M1 1 L8 6.5 L1 12 Z" fill="none" stroke="#444" stroke-width="1.2"/></svg>Search</h3>
        <div class="search-field"></div>
        <button class="button">Search</button>
      </section>

      <section class="panel widget" style="top:402px;height:74px">
        <h3 class="widget-title"><svg width="9" height="13" viewBox="0 0 9 13"><path d="M1 1 L8 6.5 L1 12 Z" fill="none" stroke="#444" stroke-width="1.2"/></svg>Categories</h3>
        <ul class="cat-list">
          <li><svg width="12" height="12" viewBox="0 0 12 12"><circle cx="6" cy="6" r="5" fill="none" stroke="#9a8a5a"/><path d="M4 6 H8 M6.5 4.5 L8 6 L6.5 7.5" stroke="#9a8a5a" fill="none"/></svg><a href="#">Uncategorized</a></li>
        </ul>
      </section>

      <section class="panel widget" style="top:490px;height:30px"></section>
    </aside>

    <main>
      <article class="panel post" style="top:118px;height:287px">
        <h2 class="post-title">Välkommen till penselbo.com!</h2>
        <p class="post-meta">June 1st, 2010 | Author: <a href="#">admin</a> | <a href="#">Edit</a></p>
        <div class="post-body">
          <div class="feature-image" role="img" aria-label="Penslar i en burk"></div>
          <p>Här hittar ni information om akvarellmåleriet, tips på utställningar mm och mitt galleri. Varmt välkomna att titta in! Jag har inte lagt ut priser på mina tavlor, då de inte i första hand är till försäljning, men om ni önskar höra er för om en tavla eller lägga en beställning så är det bara att kontakta mig!</p>
        </div>
        <div class="post-footer">Posted in <a href="#">Uncategorized</a> | <a href="#">1 Comment »</a></div>
      </article>

      <section class="panel category-block first">
        <p class="category-label">Kategori</p>
        <h2 class="category-title">Tavlor Målade I Akvarell</h2>
        <div class="category-body">
          <div class="category-image landscape" role="img" aria-label="Akvarellmålning av landskap"></div>
          <p>Akvarell är en av de mest spännande tekniker inom målningen.</p>
        </div>
      </section>

      <section class="panel category-block second">
        <p class="category-label">Kategori</p>
        <h2 class="category-title">Utställningar</h2>
        <div class="category-body">
          <div class="category-image exhibit" role="img" aria-label="Tavlor på en utställning"></div>
          <p>Tips på aktuella utställningar och besök i galleriet.</p>
        </div>
      </section>
    </main>
  </div>
</body>
</html>
```